Bref créative
Business cards and letterhead for a veterinary hospital
Marlow Ridge Veterinary Hospital
Professional
Glen H. Barrett, DVM, DABVP
Board certified, Canine and Feline Practice
5720 FM 916
Alden Falls, TX 75899
mrvhvet@fenmail.example
www.marlowridgevet.example

```html
<!DOCTYPE html>
<html lang="en">
<head>
<meta charset="utf-8">
<title>Marlow Ridge Veterinary Hospital – Business Card</title>
<link rel="stylesheet" href="https://fonts.googleapis.com/css2?family=Open+Sans:wght@400;600;700&display=swap">
<style>
  :root {
    --bg: #e4e4e4;
    --card: #ffffff;
    --navy: #1d3f7a;
    --gold: #a57a3c;
    --ink: #3f4650;
  }
  * { box-sizing: border-box; margin: 0; padding: 0; }
  html, body { width: 1200px; height: 607px; overflow: hidden; }
  body {
    background: var(--bg);
    font-family: "Open Sans", Arial, sans-serif;
    position: relative;
  }
  .card {
    position: absolute;
    top: 150px;
    width: 520px;
    height: 300px;
    background: var(--card);
    overflow: hidden;
    box-shadow: 0 2px 6px rgba(0,0,0,0.12);
  }
  .card--front { left: 50px; }
  .card--back { left: 630px; }
  .edge-band {
    position: absolute;
    right: 0; top: 0;
    width: 48px; height: 300px;
  }
  .holder { position: absolute; left: 32px; top: 34px; }
  .holder__name { color: var(--gold); font-weight: 700; font-size: 13px; }
  .holder__title { color: var(--navy); font-size: 10.5px; margin-top: 3px; }
  .contact {
    position: absolute; left: 32px; top: 190px;
    color: var(--ink); font-size: 10.5px; line-height: 16px;
  }
  .contact__row { display: flex; align-items: center; gap: 6px; }
  .contact__icon { width: 10px; height: 10px; flex: none; }
  .brand {
    color: var(--navy); font-weight: 600; text-transform: uppercase;
    text-align: center; line-height: 1.15;
  }
  .brand__main { display: block; font-size: 20px; letter-spacing: 1px; }
  .brand__sub { display: block; font-size: 10px; letter-spacing: 1.5px; }
  .card--front .brand { position: absolute; left: 235px; top: 142px; width: 220px; }
  .back-stack {
    position: absolute; left: 260px; top: 150px;
    transform: translate(-50%, -50%) rotate(-90deg);
    display: flex; flex-direction: column; align-items: center; gap: 12px;
    white-space: nowrap;
  }
  .back-url { color: var(--gold); font-size: 13px; letter-spacing: 0.5px; }
</style>
</head>
<body>

<section class="card card--front">
  <div class="holder">
    <p class="holder__name">Glen H. Barrett, DVM, DABVP</p>
    <p class="holder__title">Board certified, Canine and Feline Practice</p>
  </div>

  <div class="contact">
    <p>5720 FM 916</p>
    <p>Alden Falls, TX 75899</p>
    <p class="contact__row">
      <svg class="contact__icon" viewBox="0 0 10 10"><path d="M2 1l2 2-1 1.2c.6 1.2 1.6 2.2 2.8 2.8L7 6l2 2-1.3 1.3C4.5 9 1 5.5.7 2.3z" fill="var(--navy)"/></svg>
      Tel. 214-555-0142
    </p>
    <p class="contact__row">
      <svg class="contact__icon" viewBox="0 0 10 10"><rect x="0.5" y="2" width="9" height="6" fill="none" stroke="var(--navy)"/><path d="M0.5 2l4.5 3.5L9.5 2" fill="none" stroke="var(--navy)"/></svg>
      Email: mrvhvet@fenmail.example
    </p>
    <p class="contact__row">
      <svg class="contact__icon" viewBox="0 0 10 10"><circle cx="5" cy="5" r="4.3" fill="none" stroke="var(--navy)"/><path d="M0.7 5h8.6M5 0.7c-2.4 2.6-2.4 6 0 8.6M5 0.7c2.4 2.6 2.4 6 0 8.6" fill="none" stroke="var(--navy)" stroke-width="0.8"/></svg>
      www.marlowridgevet.example
    </p>
  </div>

  <p class="brand">
    <span class="brand__main">Marlow Ridge</span>
    <span class="brand__sub">Veterinary Hospital</span>
  </p>

  <svg class="edge-band" viewBox="0 0 48 300" preserveAspectRatio="none" aria-hidden="true">
    <path d="M48 0 L30 0 Q6 150 30 300 L48 300 Z" fill="var(--navy)"/>
    <path d="M26 0 Q2 150 26 300" fill="none" stroke="var(--gold)" stroke-width="4"/>
  </svg>
</section>

<section class="card card--back">
  <div class="back-stack">
    <p class="brand">
      <span class="brand__main">Marlow Ridge</span>
      <span class="brand__sub">Veterinary Hospital</span>
    </p>
    <p class="back-url">www.marlowridgevet.example</p>
  </div>

  <svg class="edge-band" viewBox="0 0 48 300" preserveAspectRatio="none" aria-hidden="true">
    <path d="M48 0 L30 0 Q6 150 30 300 L48 300 Z" fill="var(--navy)"/>
    <path d="M26 0 Q2 150 26 300" fill="none" stroke="var(--gold)" stroke-width="4"/>
  </svg>
</section>

</body>
</html>
```